Pinecrest Heat company

we are a renewable energy provider that specialise in Biomass
we want to promote our business in the rural and agricultural areas.
I have attached a document with the word content that needs to be on each side, they are specific and need to be exactly whats written. each page relates to each side of the flyer, one is for domestic biomass and one is for commercial biomass, my company logo is attached and so is the manufacturers logo and a picture of the boilers we install. my website is www.pinecrestheatcompany.example if you need to see our general image/branding.
rural / agricultural / off grid.
Business

```html
<!DOCTYPE html>
<html lang="en">
<head>
<meta charset="utf-8">
<title>Pinecrest Heat company – Domestic Renewable Heat Incentive</title>
<link rel="stylesheet" href="https://fonts.googleapis.com/css2?family=Roboto+Condensed:wght@700&family=Open+Sans:wght@400;600;700&display=swap">
<style>
  :root {
    --brand-green: #21a54f;
    --deep-green: #1d5c2c;
    --lime: #c6d92b;
    --ink: #1f1f1f;
    --white: #ffffff;
    --logo-dark: #1e2420;
    --box-grey: #e9e9e9;
    --rule-grey: #b9b9b9;
  }
  * { margin: 0; padding: 0; box-sizing: border-box; }
  html, body { width: 851px; height: 1200px; overflow: hidden; background: var(--white); }
  .flyer {
    position: relative; width: 851px; height: 1200px; overflow: hidden;
    font-family: "Open Sans", Arial, sans-serif; color: var(--ink); background: var(--white);
  }
  .title {
    position: absolute; top: 22px; left: 0; width: 851px; text-align: center;
    font-family: "Roboto Condensed", "Arial Narrow", sans-serif; font-weight: 700;
    font-size: 66px; line-height: 60px; color: var(--brand-green); letter-spacing: 0.5px;
  }
  .tagline {
    position: absolute; top: 176px; left: 0; width: 851px; padding-left: 10px; text-align: center;
    font-size: 17px; letter-spacing: 0.6px; color: var(--ink);
  }
  .grass-band {
    position: absolute; top: 213px; left: 0; width: 851px; height: 494px;
    background:
      radial-gradient(ellipse at 78% 35%, rgba(160,205,110,0.55), transparent 55%),
      radial-gradient(ellipse at 20% 70%, rgba(40,110,45,0.7), transparent 60%),
      linear-gradient(180deg, #2f7a32 0%, #4e9a3c 40%, #3c8a35 75%, #2c6e2c 100%);
  }
  .brand-badge {
    position: absolute; top: 160px; left: 607px; width: 200px; height: 200px; border-radius: 50%;
    background: var(--logo-dark); border: 6px solid var(--lime);
    display: flex; align-items: center; justify-content: center; text-align: center;
  }
  .brand-badge span {
    font-family: "Open Sans", Arial, sans-serif; font-weight: 600; font-size: 20px; line-height: 26px;
    color: var(--brand-green); width: 150px;
  }
  .headline {
    position: absolute; top: 236px; left: 44px; width: 540px;
    font-weight: 700; font-size: 24.5px; line-height: 33px; color: var(--white);
  }
  .benefits { position: absolute; top: 362px; left: 44px; list-style: none; color: var(--white); }
  .benefits li {
    display: flex; align-items: center; font-weight: 600; font-size: 15.5px; line-height: 24px;
  }
  .benefits svg { width: 14px; height: 14px; margin-right: 10px; flex: none; }
  .facts {
    position: absolute; top: 483px; left: 27px; width: 800px; height: 144px;
    background: linear-gradient(180deg, #ffffff 0%, var(--box-grey) 100%);
    border: 2px solid var(--white); border-radius: 18px;
    box-shadow: 0 2px 6px rgba(0,0,0,0.35); display: flex; padding: 12px 0;
  }
  .fact {
    font-weight: 700; font-size: 15.5px; line-height: 21px; color: var(--ink);
    padding: 2px 16px;
  }
  .fact + .fact { border-left: 1.5px solid var(--rule-grey); }
  .fact--subsidy { width: 314px; }
  .fact--cost { width: 228px; }
  .fact--profit { flex: 1; text-align: justify; }
  .call-line {
    position: absolute; top: 638px; left: 44px; width: 440px;
    font-size: 17.5px; line-height: 24px; color: var(--white);
  }
  .phone {
    position: absolute; top: 642px; left: 548px;
    font-family: "Roboto Condensed", "Arial Narrow", sans-serif; font-weight: 700;
    font-size: 38px; line-height: 40px; color: var(--white); letter-spacing: 1px;
  }
  .product-scene {
    position: absolute; top: 707px; left: 0; width: 851px; height: 443px;
    background:
      radial-gradient(ellipse at 80% 55%, rgba(255,150,30,0.9), rgba(230,80,10,0.5) 28%, transparent 55%),
      radial-gradient(ellipse at 25% 50%, rgba(200,60,50,0.55), transparent 40%),
      radial-gradient(ellipse at 45% 95%, rgba(205,170,120,0.6), transparent 45%),
      linear-gradient(180deg, #050505 0%, #120a05 70%, #2a1a10 100%);
  }
  .footer {
    position: absolute; top: 1150px; left: 0; width: 851px; height: 50px;
    background: var(--deep-green); display: flex; align-items: center; justify-content: space-between;
    padding: 0 24px 0 44px; color: var(--white);
  }
  .footer .email { font-size: 17px; }
  .footer .web { font-family: "Open Sans", Arial, sans-serif; font-weight: 700; font-size: 22px; letter-spacing: 0.3px; }
</style>
</head>
<body>
<div class="flyer">
  <h1 class="title">The Domestic Renewable<br>Heat Incentive</h1>
  <p class="tagline">PINECREST HEAT THE FUTURE IS BIOMASS !</p>

  <div class="grass-band" role="img" aria-label="Soft-focus green grass background"></div>

  <div class="brand-badge"><span>Pinecrest Heat company</span></div>

  <p class="headline">Get a new biomass boiler paid for by the government over a 7 year period and save save save for years to come…</p>

  <ul class="benefits">
    <li><svg viewBox="0 0 14 14"><circle cx="6" cy="6" r="4.5" fill="none" stroke="#fff" stroke-width="2"/><line x1="9.5" y1="9.5" x2="13" y2="13" stroke="#fff" stroke-width="2"/></svg>Biomass is cheaper than mains gas</li>
    <li><svg viewBox="0 0 14 14"><circle cx="6" cy="6" r="4.5" fill="none" stroke="#fff" stroke-width="2"/><line x1="9.5" y1="9.5" x2="13" y2="13" stroke="#fff" stroke-width="2"/></svg>It's 40% cheaper than Heating Oil</li>
    <li><svg viewBox="0 0 14 14"><circle cx="6" cy="6" r="4.5" fill="none" stroke="#fff" stroke-width="2"/><line x1="9.5" y1="9.5" x2="13" y2="13" stroke="#fff" stroke-width="2"/></svg>and 50% cheaper than LPG</li>
    <li><svg viewBox="0 0 14 14"><circle cx="6" cy="6" r="4.5" fill="none" stroke="#fff" stroke-width="2"/><line x1="9.5" y1="9.5" x2="13" y2="13" stroke="#fff" stroke-width="2"/></svg>and we can fix the cost of your biomass pellet fuel supply for 5 years!</li>
  </ul>

  <div class="facts">
    <p class="fact fact--subsidy">The 7-year RHI subsidy for a typical home with an EPC deemed heat demand of 25,000kw per annum = 25,000 x 12.2p = £3,050 per year x 7 years = £21,350!!</p>
    <p class="fact fact--cost">Typical installation cost for a Alpwarm 26kw manual feed biomass boiler is £15k</p>
    <p class="fact fact--profit">Potential profit just from the Domestic RHI = £6,350 and then you save money on your heating for years to come.</p>
  </div>

  <p class="call-line">Find out how you can get your share of this lucrative government backed scheme today by calling</p>
  <p class="phone">0113 496 0750</p>

  <div class="product-scene" role="img" aria-label="Red and white biomass boiler units beside a pile of wood pellets and burning pellet flames on a black background"></div>

  <footer class="footer">
    <span class="email">enquiries@pinecrestheatcompany.example</span>
    <span class="web">www.pinecrestheatcompany.example</span>
  </footer>
</div>
</body>
</html>
```